An Iconic transformation in mattress design and comfort.

“An iconic transformation in mattress design and comfort”
We are Not Kidding here!!
This is an upstart Company, PIRZO7, LLC
Our Slogan
“dream-PIRZO”

We need an outstanding web design for an outstanding product.

It took 8 years to design this bed. It was originally designed by its owner for its owner, I continue to use it every day.

With our innovative patent pending support system, with quality throughout, simplicity in design, affordable, and proudly made here in the USA, we offer a product that is superior to anything that is in the market place now. The materials that are used deviate from the industry standard, and for good reason, our product feels incredibly plush, soft, but yet provides support that can be adjusted in a simple manor, a product that will last a lifetime.
Really, why go to work if you can lay in this bed all day; you'll want to work from home! A quick nap, you'll be in heaven.

Overall Web design:
We like the web site “taltrunex.com”, sleek, modern, a site that seems to add credibility to their product by issuing registration numbers for their tops, not a bad idea for our beds. Its important to understand that this industry is filled with smoke and mirrors, over pricing, very poor quality, and show rooms filled with sales people that are piranhas.; we seek to distance ourselves! This company will sell its product not in the traditional show room but online. Please also see these websites: www.brimvora.com, www.nudlet.com

Last thing I want to see is a another website filled with beds, what to do? Well perhaps a few shots of our beds is ok, after all thats what we are selling. An idea here; I was listening to a news show, this man decided to tell his story with tattoos on his own body! Interesting, different approach (not that I'm into tattoos); website design with innovation through simplicity and creative thinking and marketing.

The photos of our product have yet to be taken by a professional. We have yet to find a way to photograph this product in a different and innovative manner.

Target Market(s)

Millennials

Industry/Entity Type

It Company

Number of Pages Required

4 page

Font styles to use
Serif

Colors
ec1f27

Requirements
Must have
• Existing logo
Nice to have
• See project description
• Can further expand upon, upon request for specifics.
Should not have
• See project description

```html
<!DOCTYPE html>
<html lang="en">
<head>
<meta charset="utf-8">
<title>PIRZO7 — Mattress Design &amp; Comfort</title>
<link href="https://fonts.googleapis.com/css2?family=Open+Sans:wght@400;600;700&display=swap" rel="stylesheet">
<style>
:root{
  --red:#c8182f;
  --red-bright:#ec1f27;
  --ink:#1f1f1f;
  --text:#555;
  --muted:#777;
  --line:#d9d9d9;
  --soft:#f7f7f7;
  --footer-bar:#eeeeee;
  --white:#fff;
}
*{margin:0;padding:0;box-sizing:border-box}
html,body{width:1200px;height:2416px;overflow:hidden;background:var(--white)}
body{font-family:"Open Sans",Arial,sans-serif;color:var(--text);position:relative}
.abs{position:absolute}

/* header */
.site-header{position:absolute;left:0;top:0;width:1200px;height:97px;background:var(--white);border-top:3px solid var(--red)}
.brand{position:absolute;left:100px;top:22px;display:flex;align-items:center;gap:10px}
.brand-mark{width:14px;height:14px;background:var(--red);border-radius:50%}
.brand-name{font-size:32px;font-weight:700;color:var(--ink);letter-spacing:1px;line-height:1}
.brand-tag{position:absolute;left:124px;top:60px;font-size:12px;color:var(--ink)}
.call{position:absolute;right:100px;top:19px;font-size:17px;font-weight:700;color:var(--ink);display:flex;align-items:center;gap:10px}
.main-nav{position:absolute;right:100px;top:53px;display:flex;gap:34px;font-size:14px;font-weight:600;color:var(--ink)}
.main-nav .active{color:var(--red);border-bottom:2px solid var(--red);padding-bottom:4px}

/* hero */
.hero{position:absolute;left:0;top:97px;width:1200px;height:454px;overflow:hidden}
.hero-photo{position:absolute;inset:0;background:linear-gradient(100deg,#e2d9cf 0%,#b8a796 28%,#7c6450 55%,#5a4433 100%)}
.hero-wave{position:absolute;left:0;bottom:0}
.hero-title{position:absolute;right:100px;top:112px;font-size:64px;font-weight:700;color:var(--white);letter-spacing:1px}
.hero-sub{position:absolute;right:100px;top:193px;font-size:19px;font-weight:600;color:var(--white)}
.hero-btn{position:absolute;left:936px;top:260px;width:164px;height:36px;border:1px solid var(--white);color:var(--white);font-size:15px;font-weight:600;display:flex;align-items:center;justify-content:center}
.arrow{position:absolute;top:170px}

/* welcome */
.section-title{position:absolute;left:0;width:1200px;text-align:center;font-size:32px;font-weight:700;color:var(--ink)}
.section-sub{position:absolute;left:0;width:1200px;text-align:center;font-size:13px;color:var(--muted)}
.feature{position:absolute;width:270px}
.feature h3{font-size:16px;font-weight:700;color:var(--ink);margin-bottom:10px}
.feature p{font-size:12px;line-height:24px;color:var(--muted)}
.feature.left{left:117px;text-align:right}
.feature.right{left:814px}

/* story */
.story{position:absolute;left:0;top:1023px;width:1200px;height:403px;background:var(--soft)}
.video{position:absolute;left:101px;top:63px;width:492px;height:277px;background:linear-gradient(120deg,#9c8268,#d9c7b0 45%,#f1e9dd 70%,#b9a38c)}
.play{position:absolute;left:222px;top:120px;width:48px;height:34px;background:var(--red);border-radius:8px}
.play::after{content:"";position:absolute;left:19px;top:10px;border-left:13px solid var(--white);border-top:7px solid transparent;border-bottom:7px solid transparent}
.story h2{position:absolute;left:660px;top:60px;font-size:31px;font-weight:700;color:var(--ink)}
.story p{position:absolute;left:660px;width:440px;font-size:12.5px;line-height:24px;color:var(--text)}
.btn-red{position:absolute;left:660px;top:304px;width:123px;height:34px;background:var(--red);color:var(--white);font-size:14px;display:flex;align-items:center;justify-content:center}

/* gallery */
.gallery{position:absolute;left:0;top:1426px;width:1200px;height:166px;display:flex}
.gallery div{flex:1}

/* blog */
.post{position:absolute;top:1740px;width:311px}
.post-img{width:311px;height:167px}
.post h3{margin-top:33px;font-size:17px;font-weight:700;color:var(--ink)}
.post p{margin-top:12px;font-size:12.5px;line-height:26px;color:var(--text);text-align:justify}

/* footer */
.site-footer{position:absolute;left:0;top:2100px;width:1200px;height:262px;border-top:3px solid var(--red)}
.f-col{position:absolute;top:45px}
.f-col h4{font-size:17px;font-weight:700;color:var(--ink);letter-spacing:1px;margin-bottom:22px}
.f-col li{list-style:none;font-size:12.5px;color:var(--text);line-height:30px}
.contact li{display:flex;gap:14px;line-height:22px;margin-bottom:14px;width:210px}
.contact svg{flex:none;margin-top:4px}
.socials{display:flex;gap:10px}
.socials span{width:26px;height:26px;border:1px solid #999;border-radius:50%}
.copyright{position:absolute;left:0;top:2362px;width:1200px;height:54px;background:var(--footer-bar);font-size:12.5px;color:var(--ink);display:flex;align-items:center;justify-content:center}
</style>
</head>
<body>

<header class="site-header">
  <div class="brand"><span class="brand-mark"></span><span class="brand-name">PIRZO7</span></div>
  <div class="brand-tag">dream-PIRZO</div>
  <div class="call">
    <svg width="16" height="16" viewBox="0 0 16 16"><rect width="16" height="16" rx="3" fill="var(--red)"/><path d="M5 4c1 0 1.5 2 1 2.5S6 8 8 10s2.5.5 3 1 .5 1.5-.5 2C8 14 3 9 4 5c.2-.6.5-1 1-1z" fill="#fff"/></svg>
    CALL US 800-555-0147
  </div>
  <nav class="main-nav">
    <span class="active">HOME</span><span>ABOUT US</span><span>WHY US</span><span>SERVICE</span><span>GALLERY</span><span>QUALITY</span><span>STORE</span><span>CONTACT US</span>
  </nav>
</header>

<section class="hero">
  <div class="hero-photo" role="img" aria-label="Mattress on a bed base in a warm room with a fireplace"></div>
  <svg class="arrow" style="left:36px" width="30" height="70" viewBox="0 0 30 70"><path d="M28 2 2 35l26 33" stroke="#fff" stroke-width="2" fill="none"/></svg>
  <svg class="arrow" style="right:36px" width="30" height="70" viewBox="0 0 30 70"><path d="M2 2l26 33L2 68" stroke="#fff" stroke-width="2" fill="none"/></svg>
  <h1 class="hero-title">DREAM - PIRZO</h1>
  <div class="hero-sub">An iconic transformation in mattress design &amp; comfort</div>
  <div class="hero-btn">GET MORE INFO</div>
  <svg class="hero-wave" width="1200" height="70" viewBox="0 0 1200 70" preserveAspectRatio="none">
    <path d="M0 12C200 55 380 60 600 35S1000 0 1200 18V70H0Z" fill="var(--red)"/>
    <path d="M0 18C200 60 380 66 600 41S1000 6 1200 24V70H0Z" fill="#fff"/>
  </svg>
</section>

<h2 class="section-title" style="top:603px">WELCOME TO PIRZO</h2>
<div class="section-sub" style="top:648px">It is a long established fact that a reader will be distracted by the readable</div>

<svg class="abs" style="left:0;top:700px" width="1200" height="280" viewBox="0 0 1200 280">
  <g stroke="var(--line)" fill="#fff">
    <line x1="432" y1="138" x2="462" y2="138"/><line x1="736" y1="138" x2="768" y2="138"/>
    <rect x="432" y="28" width="34" height="34" transform="rotate(45 449 45)"/>
    <rect x="734" y="28" width="34" height="34" transform="rotate(45 751 45)"/>
    <rect x="432" y="196" width="34" height="34" transform="rotate(45 449 213)"/>
    <rect x="734" y="196" width="34" height="34" transform="rotate(45 751 213)"/>
  </g>
  <rect x="516" y="54" width="168" height="168" transform="rotate(45 600 138)" fill="var(--red)"/>
  <rect x="530" y="68" width="140" height="140" transform="rotate(45 600 138)" fill="none" stroke="#fff" stroke-opacity=".6"/>
  <text x="600" y="144" text-anchor="middle" font-family="Open Sans, sans-serif" font-weight="700" font-size="24" fill="#fff">PIRZO7</text>
  <text x="600" y="162" text-anchor="middle" font-family="Open Sans, sans-serif" font-size="9" fill="#fff">dream-PIRZO</text>
  <path d="M449 52l-7-7a4 4 0 0 1 7-5 4 4 0 0 1 7 5z" fill="#222"/>
  <path d="M745 37v16M745 38h12l-2 4 2 4h-12" stroke="#222" stroke-width="2" fill="#222"/>
  <path d="M441 206h3l3 9h8l2-6h-12" stroke="#222" stroke-width="2" fill="none"/><circle cx="448" cy="219" r="1.6" fill="#222"/><circle cx="454" cy="219" r="1.6" fill="#222"/>
  <circle cx="751" cy="213" r="7" stroke="#222" stroke-width="2" fill="none"/><path d="M751 209v4h3" stroke="#222" stroke-width="1.6" fill="none"/>
</svg>

<div class="feature left" style="top:706px"><h3>LOVED WORLDWIDE</h3><p>It is a long established fact that a reader will be distracted by the readable content of a page</p></div>
<div class="feature right" style="top:706px"><h3>DESIGNED TO BE TOUCHED</h3><p>It is a long established fact that a reader will be distracted by the readable content</p></div>
<div class="feature left" style="top:876px"><h3>OUR STORE</h3><p>It is a long established fact that a reader will be distracted by the readable content of a page</p></div>
<div class="feature right" style="top:876px"><h3>LIFETIME WARRANTY</h3><p>It is a long established fact that a reader will be distracted by the readable content</p></div>

<section class="story">
  <div class="video" role="img" aria-label="Video still of a bright hotel-style bedroom with a made bed"><span class="play"></span></div>
  <h2>WE ARE NOT KIDDING HERE!!</h2>
  <p style="top:120px">It took 8 years to design this bed. It was originally designed by its owner for its owner, I continue to use it every day.</p>
  <p style="top:180px">With our innovative patent pending support system, with quality throughout, simplicity in design, affordable, and proudly made here in the USA, we offer a product that is superior to anything that is in the market place now. The materials that are used deviate from the industry standard</p>
  <div class="btn-red">Read More</div>
</section>

<div class="gallery">
  <div role="img" aria-label="Mattress in front of a fireplace" style="background:linear-gradient(180deg,#6b5848,#cfcac4 55%,#3b3a3e)"></div>
  <div role="img" aria-label="Mattress corner close-up" style="background:linear-gradient(180deg,#4a3d33,#dcd8d2 55%,#2f2e33)"></div>
  <div role="img" aria-label="Mattress on carpet" style="background:linear-gradient(180deg,#7a624e,#d6d1ca 55%,#3a383d)"></div>
  <div role="img" aria-label="Mattress side panel" style="background:linear-gradient(180deg,#8b6a4c,#e2ddd6 45%,#35343a)"></div>
  <div role="img" aria-label="Soft mattress top close-up" style="background:linear-gradient(120deg,#7a6556,#efe9e1 60%,#d9cfc2)"></div>
</div>

<h2 class="section-title" style="top:1642px">OUR RECENT BLOG POST</h2>
<div class="section-sub" style="top:1688px">There are many variations of passages Lorem Ipsum</div>

<article class="post" style="left:100px">
  <div class="post-img" role="img" aria-label="Person sleeping peacefully on a white pillow" style="background:linear-gradient(180deg,#e9e6e2,#f6f4f1 60%,#fff)"></div>
  <h3>SED PERSPICIATIS UNDE OMNIS</h3>
  <p>Lorem ipsum dolor sit amet, consectetuer. Proin gravida nibh vel velit auctor aliquet. the far Aenean sollicitudi ravida.Lorem ipsum dolor sit amet,</p>
</article>
<article class="post" style="left:446px">
  <div class="post-img" role="img" aria-label="Couple outdoors receiving a new mattress delivery" style="background:linear-gradient(180deg,#c9b8a2,#e6e0d8 50%,#7f8d5a)"></div>
  <h3>SED PERSPICIATIS UNDE OMNIS</h3>
  <p>Lorem ipsum dolor sit amet, consectetuer. Proin gravida nibh vel velit auctor aliquet. the far Aenean sollicitudi ravida.Lorem ipsum dolor sit amet,</p>
</article>
<article class="post" style="left:791px">
  <div class="post-img" role="img" aria-label="Family playing together under white bed sheets" style="background:linear-gradient(180deg,#f3f1ee,#e8e2da 55%,#c9b9a6)"></div>
  <h3>SED PERSPICIATIS UNDE OMNIS</h3>
  <p>Lorem ipsum dolor sit amet, consectetuer. Proin gravida nibh vel velit auctor aliquet. the far Aenean sollicitudi ravida.Lorem ipsum dolor sit amet,</p>
</article>

<footer class="site-footer">
  <div class="f-col contact" style="left:98px">
    <h4>CONTACT US</h4>
    <ul>
      <li><svg width="10" height="12" viewBox="0 0 10 12"><path d="M5 12S0 6.5 0 4.5a5 5 0 0 1 10 0C10 6.5 5 12 5 12z" fill="var(--red)"/><circle cx="5" cy="4.5" r="1.8" fill="#fff"/></svg>2000 years old, Anselm Varkow, a Latin professor at</li>
      <li><svg width="12" height="12" viewBox="0 0 16 16"><path d="M4 1c1.5 0 2 3 1.3 3.7S5 7 7.5 9.5 10.6 10 11.3 10.7 14 12 14 13c-1 2-4 2.5-8-1.5S1 4 2 2.5C2.5 1.5 3 1 4 1z" fill="var(--red)"/></svg>Phone - 0400 555 318</li>
      <li><svg width="12" height="12" viewBox="0 0 12 12"><rect y="4" width="12" height="7" rx="1" fill="var(--red)"/><rect x="3" y="1" width="6" height="4" fill="var(--red)"/></svg>Fax - 020 555 7741</li>
      <li><svg width="13" height="10" viewBox="0 0 13 10"><rect x=".5" y=".5" width="12" height="9" fill="none" stroke="var(--red)"/><path d="M.5.5l6 5 6-5" fill="none" stroke="var(--red)"/></svg>E-mail - hello@pirzo7.example</li>
    </ul>
  </div>
  <div class="f-col" style="left:369px"><h4>QUICK LINKS</h4><ul><li>Home</li><li>About Us</li><li>Products</li><li>Blog</li></ul></div>
  <div class="f-col" style="left:536px"><h4>OUR POLICY</h4><ul><li>Shop</li><li>Contact</li><li>Website Policies</li></ul></div>
  <div class="f-col" style="left:727px"><h4>COMMUNITY</h4><ul><li>Guidlines</li><li>Terms &amp; conditions</li><li>privacy policy</li><li>site map</li></ul></div>
  <div class="f-col" style="left:909px"><h4>SOCIAL MEDIA</h4><div class="socials"><span></span><span></span><span></span><span></span><span></span><span></span></div></div>
</footer>
<div class="copyright">Copyrights@2017Compny name , All rights Reserved</div>

</body>
</html>
```